Qorvant Flyer Design Project

We need a new flyer design for our company based in Australia. We provide Business Valuations for small businesses. The flyer should follow the same colours and theme as our website www.qorvant.com.au and our logo. The design should communicate a professional financial services company. It should be a simple design (not too 'busy') and have a sleek and professional feel to it. It will be used to send to prospective clients and referral sources to tell about our company and prompt them to call us or visit our website.

Target Market(s)

Business owners and people working in financial services (accountants, financial planners etc)

Industry/Entity Type

Financial

Requirements
Must have
• Must be DL double sided, (99mm x 210mm) and use CMYK colours. Must contain trim marks for printer and be print ready.

```html
<!DOCTYPE html>
<html lang="en">
<head>
<meta charset="utf-8">
<title>Qorvant DL Flyer</title>
<link rel="stylesheet" href="https://fonts.googleapis.com/css2?family=Arimo:wght@400;700&family=Roboto+Condensed:wght@700&display=swap">
<style>
  :root{
    --page:#ffffff;
    --blue-deep:#083578;
    --blue-mid:#0f56a8;
    --blue-bright:#1d7cc8;
    --sky:#9fd3f2;
    --white:#ffffff;
    --cream:#eef2cf;
    --lime:#c9e06a;
    --ink:#0d3f86;
    --panel-light:#e7f4fc;
  }
  *{box-sizing:border-box;margin:0;padding:0}
  html,body{width:1172px;height:1200px;overflow:hidden;background:var(--page)}
  body{position:relative;font-family:"Arimo",Arial,sans-serif;color:var(--white)}
  .panel{
    position:absolute;top:28px;height:1143px;width:537px;overflow:hidden;
    background:
      linear-gradient(115deg,rgba(255,255,255,0) 40%,rgba(255,255,255,.07) 52%,rgba(255,255,255,0) 64%),
      linear-gradient(180deg,var(--blue-deep) 0%,var(--blue-mid) 55%,var(--blue-bright) 100%);
  }
  .panel--front{left:34px}
  .panel--back{left:597px}

  /* front */
  .brand-mark{position:absolute;left:145px;top:105px;width:262px;height:262px;border-radius:50%;
    background:radial-gradient(circle at 40% 35%,#3a8fd6,#0c4a9a 70%);border:5px solid var(--sky)}
  .brand-name{position:absolute;left:0;width:100%;top:420px;text-align:center;
    font-weight:700;font-size:104px;letter-spacing:-1px;color:var(--sky)}
  .tagline{position:absolute;left:41px;top:632px;font-size:50px;line-height:61px;font-weight:400}
  .badge{position:absolute;left:304px;top:630px;width:196px;height:196px;border-radius:50%;
    border:5px solid var(--white);background:radial-gradient(circle at 50% 40%,#1a6cc0,#08397f);
    display:flex;flex-direction:column;align-items:center;justify-content:center;
    font-family:"Roboto Condensed","Arial Narrow",sans-serif;font-weight:700;font-size:50px;line-height:52px}
  .badge .fix{color:var(--cream)}
  .badge .ed{color:var(--lime)}
  .contact-card{position:absolute;left:0;bottom:0;width:100%;height:228px;border-radius:40px 40px 0 0;
    background:linear-gradient(180deg,var(--white),var(--panel-light))}
  .contact-list{position:absolute;left:41px;top:42px;list-style:none;color:var(--ink);font-size:20px;line-height:26.5px}
  .contact-list li{display:flex;align-items:center;gap:8px}
  .contact-list svg{width:16px;height:16px;flex:none}
  .contact-art{position:absolute;left:318px;top:34px;width:180px;height:140px;border-radius:12px;
    background:linear-gradient(135deg,#d9dee4,#8a939c)}

  /* back */
  .back-title{position:absolute;left:51px;top:48px;font-size:77px;line-height:77px;font-weight:700;color:var(--cream)}
  .reasons{position:absolute;left:51px;top:266px;width:460px;list-style:none;font-size:20.5px;line-height:25.5px}
  .reasons li{position:relative;padding-left:17px;margin-bottom:8px}
  .reasons li::before{content:"•";position:absolute;left:0}
  .reasons b{font-weight:700}
  .team-art{position:absolute;left:52px;top:808px;width:440px;height:250px;border-radius:10px;
    background:linear-gradient(180deg,rgba(120,180,230,.0),rgba(120,180,230,.35))}
  .cta{position:absolute;left:43px;top:976px;font-weight:700;line-height:40px}
  .cta .lead{font-size:34px}
  .cta .small{font-size:26px}
  .cta .big{font-size:33px}
</style>
</head>
<body>
  <section class="panel panel--front">
    <div class="brand-mark"></div>
    <div class="brand-name">Qorvant</div>
    <h2 class="tagline">Small<br>Business<br>Valuation<br>Experts</h2>
    <div class="badge"><span><span class="fix">FIX</span><span class="ed">ED</span></span><span class="fix">PRICE</span></div>
    <div class="contact-card">
      <ul class="contact-list">
        <li><svg viewBox="0 0 16 16"><path fill="#0d3f86" d="M2 6c0-2 3-3 6-3s6 1 6 3l-3 1-1-2H6L5 7 2 6zm2 2h8l1 5H3z"/></svg>1300 482 615</li>
        <li><svg viewBox="0 0 16 16"><path fill="#0d3f86" d="M4 1h8v5H4zM2 7h12v7H2zm2 2v2h8V9z"/></svg>07 5521 3046</li>
        <li><svg viewBox="0 0 16 16"><text x="0" y="13" font-size="15" fill="#0d3f86" font-family="Arimo,sans-serif">@</text></svg>info@qorvant.com.au</li>
        <li><svg viewBox="0 0 16 16"><circle cx="8" cy="8" r="6" fill="none" stroke="#0d3f86" stroke-width="1.5"/><path d="M2 8h12M8 2c-3 4-3 8 0 12M8 2c3 4 3 8 0 12" fill="none" stroke="#0d3f86"/></svg>www.qorvant.com.au</li>
        <li>ABN – 41 903 276 158</li>
      </ul>
      <div class="contact-art" role="img" aria-label="Illustration of a desk telephone beside a waving business figure"></div>
    </div>
  </section>

  <section class="panel panel--back">
    <h1 class="back-title">Why use<br>Qorvant?</h1>
    <ul class="reasons">
      <li><b>Qualified Accountant spends time reviewing every business</b></li>
      <li><b>Specialised</b> – valuing small businesses is all we do</li>
      <li>We use our experience to compare and benchmark similar businesses across Australia</li>
      <li>A valuation appraisal report emailed to you with our comments and valuation estimate</li>
      <li><b>Five business day turnaround!</b></li>
      <li>A follow up phone call from an Accountant to discuss the valuation and answer any questions you have</li>
      <li><b>Fixed price of only $540 (+gst)</b></li>
      <li>Our clients include Business Buyers and Sellers, Accountants, Solicitors, Financial Planners, Franchisors and Franchisees.</li>
    </ul>
    <div class="team-art" role="img" aria-label="Illustration of a graduate figure presenting at a board to a small audience"></div>
    <div class="cta">
      <div class="lead">FOR MORE INFO</div>
      <div><span class="small">call</span> <span class="big">1300 482 615</span></div>
      <div><span class="small">visit</span> <span class="big">www.qorvant.com.au</span></div>
    </div>
  </section>
</body>
</html>
```